Tamaru Peruvian Cuisine needs a take-out menu

We need a new tri-fold 8.5"x11" take out menu for a Peruvian restaurant based in New Rochelle, NY. We have a vast selections of dishes from appetizers, seafood based dishes, desserts, Peruvian ceviches and more. We have attached the following:

Restaurant information
Pictures of our dishes
Tamaru Logo in pdf format
Menu in word format
Old take out menu for reference only! (our dishes have changed)
Updates

Project Deadline Extended
Reason: Need more time to make final decision.

Industry/Entity Type

Restaurant

```html
<!DOCTYPE html>
<html lang="en">
<head>
<meta charset="utf-8">
<title>Tamaru Peruvian Cuisine – Take-Out Menu</title>
<link rel="stylesheet" href="https://fonts.googleapis.com/css2?family=Source+Sans+3:wght@400;600;700&family=Oswald:wght@500&display=swap">
<style>
:root{
  --page:#000;
  --wood:#5b2f14;
  --wood-dark:#4a240e;
  --wood-light:#6a381a;
  --leaf:#45b048;
  --leaf-dark:#2f8f34;
  --teal:#2fae7c;
  --teal-dark:#1f8d62;
  --cream:#f7efcf;
  --white:#ffffff;
  --ink:#2a1608;
  --pill-text:#2e7a2c;
  --plate:#f3eee6;
}
*{box-sizing:border-box;margin:0;padding:0}
html,body{width:844px;height:1200px;overflow:hidden}
body{background:var(--page);font-family:"Source Sans 3",Arial,sans-serif;color:var(--white);position:relative}
.spread{position:absolute;left:34px;width:784px;display:flex}
.spread-outside{top:38px;height:556px}
.spread-inside{top:625px;height:554px}
.panel{position:relative;width:261.33px;height:100%;overflow:hidden}
.wood{background:linear-gradient(180deg,var(--wood-light) 0%,var(--wood) 45%,var(--wood-dark) 100%)}
.leaf{background:radial-gradient(circle at 50% 40%,#52bc51,var(--leaf) 60%,#3aa23e)}
.teal{background:radial-gradient(circle at 50% 50%,#38b986,var(--teal) 60%,#25996b)}

.heading{position:absolute;left:16px;right:16px;height:21px;border-radius:7px;
  font-size:17px;font-weight:600;line-height:21px;text-align:center;letter-spacing:.2px}
.heading-leaf{background:var(--leaf);color:var(--white);box-shadow:0 2px 3px rgba(0,0,0,.4)}
.heading-wood{background:var(--wood);color:var(--white);box-shadow:0 2px 3px rgba(0,0,0,.35)}
.heading-white{background:var(--white);color:var(--pill-text);box-shadow:0 2px 3px rgba(0,0,0,.3)}

.list{position:absolute;left:18px;right:16px}
.item-head{display:flex;justify-content:space-between;align-items:baseline;font-size:9.6px;font-weight:600;line-height:1.15;white-space:nowrap}
.item-head .note{font-size:6.6px;font-weight:400;margin-left:4px}
.item-head .name{flex:1}
.item-head .variants{font-size:7px;font-weight:400}
.item-head .variants b{font-size:9.6px;font-weight:600}
.desc{font-size:6.4px;line-height:1.28;margin-top:1px;opacity:.95}
.dark-text{color:var(--ink)}
.dark-text .desc{color:#2d2a14}

.photo{position:absolute;left:0;right:0}
.curve{position:absolute;left:0;width:100%;display:block}

.phone{font-family:"Oswald",Arial,sans-serif;font-weight:500;color:var(--white);letter-spacing:.5px;
  text-shadow:-1px -1px 0 #333,1px -1px 0 #333,-1px 1px 0 #333,1px 1px 0 #333}

.brand-name{font-size:26px;font-weight:600;color:var(--leaf-dark);line-height:1}
.brand-badge{position:absolute;display:flex;align-items:center;justify-content:center}
</style>
</head>
<body>

<section class="spread spread-outside">

  <div class="panel wood">
    <div class="heading heading-leaf" style="top:19px">SEAFOOD</div>
    <div class="list" style="top:50px">
      <div class="item" style="margin-bottom:8px"><div class="item-head"><span class="name">PESCADO A LO MACHO</span><span>19.95</span></div>
        <p class="desc">fried fish fillet topped with seafood in hot yellow pepper sauce, served with rice and yuccas –</p></div>
      <div class="item" style="margin-bottom:8px"><div class="item-head"><span class="name">PESCADO SUDADO</span><span>16.95</span></div>
        <p class="desc">corvina fish stew, in hot yellow pepper, tomatoes, onions, served with yuccas and rice –</p></div>
      <div class="item" style="margin-bottom:8px"><div class="item-head"><span class="name">ARROZ CON MARISCOS</span><span>17.95</span></div>
        <p class="desc">peruvian style paella, red rice served with seafood</p></div>
      <div class="item" style="margin-bottom:5px"><div class="item-head"><span class="name">ARROZ CHAUFA</span><span class="variants">Mariscos-<b>17.95</b>, Camarones-<b>17.95</b></span></div>
        <p class="desc">peruvian style fried rice served with choice of seafood or shrimp</p></div>
      <div class="item" style="margin-bottom:7px"><div class="item-head"><span class="name">TRUCHA FRITA</span><span>18.95</span></div>
        <p class="desc">deep fried Trout, served with white rice, fried yuccas and salsa criolla –</p></div>
      <div class="item"><div class="item-head"><span class="name">JALEA</span><span class="variants">Large- <b>28.95</b>, Small- <b>17.95</b></span></div>
        <p class="desc">deep fried mixed seafood and fish, served with fried yuccas</p></div>
    </div>
    <div class="photo" role="img" aria-label="Photo of fried chicken strips, a glass of chicha and plated Peruvian dishes with ceviche and causa" style="top:240px;bottom:0;background:radial-gradient(ellipse at 50% 55%,#e8b27a 0%,#f1e2cf 55%,var(--plate) 100%)"></div>
    <svg class="curve" style="top:230px;height:40px" viewBox="0 0 261 40" preserveAspectRatio="none" aria-hidden="true">
      <path d="M0 0H261V8C180 2 80 10 0 36Z" fill="var(--wood-dark)"/>
      <path d="M0 36C80 10 180 2 261 8V14C180 8 90 16 0 40Z" fill="var(--leaf)"/>
    </svg>
  </div>

  <div class="panel leaf">
    <div class="heading heading-wood" style="top:16px">CHICKEN</div>
    <div class="list" style="top:48px">
      <div class="item" style="margin-bottom:7px"><div class="item-head"><span class="name">1/4 POLLO</span><span>6.50</span></div><p class="desc">quarter chicken, served with two sides –</p></div>
      <div class="item" style="margin-bottom:7px"><div class="item-head"><span class="name">1/2 POLLO</span><span>8.95</span></div><p class="desc">half chicken, served with two sides –</p></div>
      <div class="item" style="margin-bottom:7px"><div class="item-head"><span class="name">1 POLLO</span><span>16.95</span></div><p class="desc">whole chicken, served with two sides –</p></div>
      <div class="item" style="margin-bottom:7px"><div class="item-head"><span class="name">POLLO LIMEÑO</span><span>20.95</span></div><p class="desc">whole chicken, served with French fries, avocado salad and yellow rice –</p></div>
      <div class="item" style="margin-bottom:7px"><div class="item-head"><span class="name">POLLO CHALACO</span><span>26.95</span></div><p class="desc">whole chicken, served with avocado salad, salchipapa and yellow rice –</p></div>
      <div class="item"><div class="item-head"><span class="name">POLLO TAMARU</span><span>30.95</span></div><p class="desc">whole chicken, served with avocado salad, arroz chaufa (chicken or steak) and salchipapa –</p></div>
    </div>
    <div class="heading heading-wood" style="top:226px">DESSERTS</div>
    <div class="list" style="top:257px">
      <div class="item" style="margin-bottom:3px"><div class="item-head"><span class="name">CREMA VOLTEADA<span class="note">(Peruvian caramel custard)</span></span><span>5.95</span></div></div>
      <div class="item" style="margin-bottom:5px"><div class="item-head"><span class="name">TRES LECHES</span><span>5.95</span></div><p class="desc">Butter cake soaked in three kinds of milk</p></div>
      <div class="item" style="margin-bottom:5px"><div class="item-head"><span class="name">TORTA HELADA</span><span>5.95</span></div><p class="desc">Sponge cake topped with strawberry jello</p></div>
      <div class="item" style="margin-bottom:3px"><div class="item-head"><span class="name">TORTA DE CHOCHOLATE<span class="note">(Chocolate cake)</span></span><span>5.95</span></div></div>
      <div class="item"><div class="item-head"><span class="name">PICARONES</span><span>5.95</span></div><p class="desc">Peruvian style sweet potato doughnut covered with syrup</p></div>
    </div>
    <div class="photo" role="img" aria-label="Photo of a whole rotisserie chicken with French fries and salad" style="top:372px;bottom:0;background:radial-gradient(ellipse at 55% 55%,#c98a4e 0%,#ead7bf 50%,var(--plate) 100%)"></div>
    <svg class="curve" style="top:362px;height:60px" viewBox="0 0 261 60" preserveAspectRatio="none" aria-hidden="true">
      <path d="M0 0H261V6C170 10 60 30 0 56Z" fill="var(--leaf)"/>
      <path d="M0 56C60 30 170 10 261 6V12C170 16 70 36 0 60Z" fill="var(--leaf-dark)"/>
    </svg>
    <div class="brand-badge" style="left:16px;top:382px;width:92px;height:60px;background:var(--cream);border:3px solid var(--wood);border-radius:50%">
      <span class="brand-name" style="font-size:17px">Tamaru</span>
    </div>
    <div class="phone" style="position:absolute;left:12px;top:516px;font-size:23px">914.555.0137</div>
  </div>

  <div class="panel wood">
    <div class="photo" role="img" aria-label="Photo of Andean mountain ruins under a blue sky" style="top:0;height:250px;background:linear-gradient(180deg,#eef2f5 0%,#c9d3d8 25%,#7f977a 55%,#5e7756 100%)"></div>
    <svg class="curve" style="top:200px;height:70px" viewBox="0 0 261 70" preserveAspectRatio="none" aria-hidden="true">
      <path d="M0 60C90 60 180 30 261 0V70H0Z" fill="var(--wood-light)"/>
      <path d="M0 50C90 52 180 22 261 -6V6C180 34 90 64 0 62Z" fill="var(--leaf)"/>
    </svg>
    <div style="position:absolute;right:20px;top:16px;font-size:9.6px;color:#333;font-weight:400">418 Harbor Ave. New Rochelle, NY 10801</div>
    <div class="phone" style="position:absolute;right:18px;top:29px;font-size:27px">914.555.0137</div>
    <div style="position:absolute;left:0;right:0;top:282px;text-align:center;font-size:27px;font-weight:600;line-height:27px;text-shadow:0 1px 2px rgba(0,0,0,.4)">AUTHENTIC<br>PERUVIAN CUISINE</div>
    <div class="brand-badge" style="left:60px;top:346px;width:142px;height:66px;background:var(--cream);border:3px solid var(--leaf);border-radius:50%">
      <span class="brand-name">Tamaru</span>
    </div>
    <div style="position:absolute;left:0;right:0;top:436px;text-align:center">
      <div style="font-size:14.5px;font-weight:600;line-height:18px">Delivery Hours:<br>Mon - Sun 11:30 am – 10 pm</div>
      <p style="font-size:9.6px;line-height:12.5px;margin:6px auto 0;width:160px">Deliveries on order of $15 or more, $5 fee for 3 miles or more Chef's specials on weekends.</p>
      <div style="font-size:14.5px;font-weight:600;margin-top:9px;letter-spacing:.4px">www.tamarunewrochelle.com</div>
    </div>
  </div>
</section>

<section class="spread spread-inside">

  <div class="panel leaf dark-text">
    <div class="heading heading-white" style="top:24px;color:var(--wood)">APPETIZERS</div>
    <div class="list" style="top:57px">
      <div class="item" style="margin-bottom:9px"><div class="item-head"><span class="name">CHICHARRON DE CALAMARES</span><span>12.95</span></div><p class="desc">crispy fried calamari served with house tartar sauce and salsa criolla</p></div>
      <div class="item" style="margin-bottom:9px"><div class="item-head"><span class="name">ANTICUCHO CARRETILLERO</span><span>15.95</span></div><p class="desc">choice chicken or cow's heart Peruvian style kebabs, served with Cusco corn and grilled potatoes. Corazon – 15.95 Pollo – 15.95</p></div>
      <div class="item" style="margin-bottom:9px"><div class="item-head"><span class="name">PALTA RELLENA</span><span class="variants">Camarones-<b>11.95</b> Pollo - <b>8.95</b></span></div><p class="desc">peruvian avocado stuffed with choice of chicken or shrimp, marinated in Peruvian spices</p></div>
      <div class="item" style="margin-bottom:10px"><div class="item-head"><span class="name">TAMAL CRIOLLO</span><span>5.95</span></div><p class="desc">peruvian chicken tamale, served with salsa criolla –</p></div>
      <div class="item" style="margin-bottom:10px"><div class="item-head"><span class="name">SALCHIPAPA</span><span>9.95</span></div><p class="desc">french fries mixed with sliced hot dogs –</p></div>
      <div class="item" style="margin-bottom:9px"><div class="item-head"><span class="name">PAPA A LA HUANCAINA</span><span>8.95</span></div><p class="desc">boiled potatoes, topped with aji amarillo and queso fresco sauce, egg, olives</p></div>
      <div class="item" style="margin-bottom:10px"><div class="item-head"><span class="name">OCOPA AREQUIPEÑA</span><span>8.95</span></div><p class="desc">boiled potatoes, topped with huacatay sauce and queso fresco, egg, olives</p></div>
      <div class="item" style="margin-bottom:10px"><div class="item-head"><span class="name">EMPANADA LIMEÑA</span><span>3.95</span></div><p class="desc">patties stuffed with choice of chicken or beef –</p></div>
      <div class="item" style="margin-bottom:9px"><div class="item-head"><span class="name">CAUSA</span><span class="variants">Camarones – <b>9.95</b>, Pollo – <b>7.95</b></span></div><p class="desc">cold mashed potato infused with key of lime juice, pressed into a cake with choice of chicken or shrimp</p></div>
      <div class="item" style="margin-bottom:9px"><div class="item-head"><span class="name">CHORITOS A LA CHALACA</span><span>10.95</span></div><p class="desc">steamed mussels topped with diced onions, tomatoes, lime juice and Cusco corn –</p></div>
      <div class="item"><div class="item-head"><span class="name">PIQUEO TAMARU</span><span>19.95</span></div><p class="desc">Dished combined of Chicharron de Calamares, Papa a la Huancaina, Choritos a la Chalaca and Causa –</p></div>
    </div>
    <div class="heading heading-white" style="top:425px;color:var(--wood)">SALADS</div>
    <div class="list" style="top:458px">
      <div class="item" style="margin-bottom:8px"><div class="item-head"><span class="name">ENSALADA DE LA CASA</span><span>6.95</span></div><p class="desc">lettuce, tomatoes, yellow peppers and zucchini –</p></div>
      <div class="item" style="margin-bottom:8px"><div class="item-head"><span class="name">ENSALADA TAMARU</span><span>7.95</span></div><p class="desc">lettuce, tomatoes, cucumbers, red onions, carrots, radish and avocado –</p></div>
      <div class="item"><div class="item-head"><span class="name">ENSALADA CESAR</span><span>8.95</span></div><p class="desc">romaine, lettuce, croutons, parmesan cheese and Tamaru's special sauce –</p></div>
    </div>
  </div>

  <div class="panel teal dark-text">
    <div class="photo" role="img" aria-label="Photo of ceviche with red onion, shrimp and white corn" style="top:0;height:96px;background:radial-gradient(ellipse at 50% 45%,#e6c3b0 0%,#f1e9df 55%,var(--plate) 100%)"></div>
    <svg class="curve" style="top:52px;height:48px" viewBox="0 0 261 48" preserveAspectRatio="none" aria-hidden="true">
      <path d="M0 10C80 46 180 44 261 20V48H0Z" fill="var(--teal)"/>
      <path d="M0 4C80 40 180 38 261 14V22C180 46 80 48 0 12Z" fill="var(--white)"/>
    </svg>
    <div class="heading heading-white" style="top:91px;left:12px;text-align:left;padding-left:6px;color:var(--ink)">SOUPS</div>
    <div class="list" style="top:124px">
      <div class="item" style="margin-bottom:6px"><div class="item-head"><span class="name">AGUADITO LIMEÑO</span><span class="variants">Large – <b>9.95</b>, Small-<b>5.95</b></span></div><p class="desc">chicken and vegetable soup mixed with rice and cilantro</p></div>
      <div class="item" style="margin-bottom:6px"><div class="item-head"><span class="name">SOPA A LA MINUTA</span><span>12.95</span></div><p class="desc">traditional milk and angel's hair pasta soup, served with beef and eggs –</p></div>
      <div class="item" style="margin-bottom:6px"><div class="item-head"><span class="name">CALDO DE GALLINA</span><span>12.95</span></div><p class="desc">hen broth with noodles, scallion, potatoes and hard-boiled egg –</p></div>
      <div class="item" style="margin-bottom:6px"><div class="item-head"><span class="name">CHUPE DE CAMARONES AREQUIPEÑO</span><span>15.95</span></div><p class="desc">shrimp soup mixed with rice, green peas, Cusco corn, milk, eggs and Peruvian spices</p></div>
      <div class="item"><div class="item-head"><span class="name">PARIHUELA DEL PUERTO</span><span>18.95</span></div><p class="desc">classic Peruvian seafood soup –</p></div>
    </div>
    <div class="heading heading-white" style="top:272px;color:var(--ink)">CEVICHES</div>
    <div class="list" style="top:299px">
      <div class="item" style="margin-bottom:6px"><div class="item-head"><span class="name">LECHE DE TIGRE</span><span>10.95</span></div><p class="desc">ceviche marinade in fresh lime juice –</p></div>
      <div class="item" style="margin-bottom:6px"><div class="item-head"><span class="name">TIRADITO EN SALSA DE AJI AMARILLO</span><span>12.95</span></div><p class="desc">sashimi style fish in yellow pepper sauce and fresh lime juice, served with Cusco corn and sweet potatoes –</p></div>
      <div class="item" style="margin-bottom:6px"><div class="item-head"><span class="name">PIQUEO CHALACO</span><span>24.95</span></div><p class="desc">dish combined of Ceviche de Pescado (Fish Ceviche) and Jalea (Fried Seafood)</p></div>
      <div class="item"><div class="item-head"><span class="name">CEVICHE</span><span class="variants">Pescado-<b>15.95</b>, Camaron-<b>17.95</b></span></div>
        <div class="item-head" style="justify-content:flex-end"><span class="variants">Mixto- <b>17.95</b>, Camaron con Pulpo – <b>18.95</b></span></div>
        <p class="desc">choice of raw fish, mixed seafood, shrimp or shrimp with octopus, marinated in fresh lime juice, served with red onions, Cusco corn and sweet potatoes</p></div>
    </div>
    <div class="heading heading-white" style="top:442px;color:var(--ink)">SIDES</div>
    <div class="list" style="top:468px">
      <div class="item-head" style="margin-bottom:3px"><span class="name">PAPAS FRITAS<span class="note">( french fries) –</span></span><span>3.95</span></div>
      <div class="item-head" style="margin-bottom:3px"><span class="name">ARROZ BLANCO O AMARILLO<span class="note">(white/yellow rice)</span></span><span>3.95</span></div>
      <div class="item-head" style="margin-bottom:3px"><span class="name">FREJOLES<span class="note">(peruvian canario beans)</span></span><span>3.95</span></div>
      <div class="item-head" style="margin-bottom:3px"><span class="name">MADUROS<span class="note">(sweet plantains)</span></span><span>3.95</span></div>
      <div class="item-head" style="margin-bottom:3px"><span class="name">TOSTONES<span class="note">(fried green plantains )</span></span><span>3.95</span></div>
      <div class="item-head"><span class="name">YUCA FRITA<span class="note">( fried yuccas )</span></span><span>3.95</span></div>
    </div>
  </div>

  <div class="panel wood">
    <div class="heading heading-leaf" style="top:17px;left:12px;right:14px">TRADITIONAL DISHES</div>
    <div class="list" style="top:54px">
      <div class="item" style="margin-bottom:7px"><div class="item-head"><span class="name">PARRILLADA MIXTA</span><span>30.95</span></div><p class="desc">dish combined of grilled NY Strip steak, anticuchos (Peruvian style kebabs), pork chops and sausage –</p></div>
      <div class="item" style="margin-bottom:7px"><div class="item-head"><span class="name">CHURRASCO EN SALSA DE CAMARONES</span><span>20.95</span></div><p class="desc">NY strip steak topped with shrimps on hot yellow pepper sauce, served with rice –</p></div>
      <div class="item" style="margin-bottom:7px"><div class="item-head"><span class="name">SECO NORTEÑO</span><span>20.95</span></div><p class="desc">slowly cooked lamb stew in aji panka sauce, served with rice and Peruvian canario beans –</p></div>
      <div class="item" style="margin-bottom:7px"><div class="item-head"><span class="name">SECO DE PATO PIURANO</span><span>17.95</span></div><p class="desc">slowly cooked duck stew in aji panka sauce, served with rice and hard-boiled yuccas –</p></div>
      <div class="item" style="margin-bottom:7px"><div class="item-head"><span class="name">TALLARINES VERDES CON CHURRASCO</span><span>18.95</span></div><p class="desc">linguine pasta in Peruvian style pesto sauce served with grilled NY Strip steak</p></div>
      <div class="item" style="margin-bottom:7px"><div class="item-head"><span class="name">TACU TACU</span><span class="variants">Churrasco – <b>18.95</b>, Lomo – <b>15.95</b></span></div><p class="desc">peruvian canario beans mixed with rice, served with choice of NY Strip steak or wok-seared beef in soy sauce</p></div>
      <div class="item" style="margin-bottom:7px"><div class="item-head"><span class="name">CHURRASCO A LO POBRE</span><span>19.95</span></div><p class="desc">NY Strip steak served with fried eggs, sweet plantains, French fries and rice</p></div>
      <div class="item" style="margin-bottom:7px"><div class="item-head"><span class="name">SALTADO</span><span class="variants">Lomo – <b>15.95</b>, Pollo – <b>13.95</b></span></div><p class="desc">choice of wok-seared steak or chicken, mixed with red onions, tomatoes, in soy sauce, served with French fries and rice</p></div>
      <div class="item" style="margin-bottom:7px"><div class="item-head"><span class="name">AEROPUERTO</span><span>18.95</span></div><p class="desc">peruvian style fried rice, mixed with noodles, chicken, beef and shrimp –</p></div>
      <div class="item" style="margin-bottom:7px"><div class="item-head"><span class="name">ARROZ CHAUFA</span><span class="variants">Carne – <b>14.95</b>, Pollo – <b>12.95</b></span></div><p class="desc">peruvian style fried rice mixed with choice of beef or chicken</p></div>
      <div class="item" style="margin-bottom:7px"><div class="item-head"><span class="name">SECO DE CARNE</span><span>15.95</span></div><p class="desc">beef ribs stew in aji panka sauce, served with rice and Peruvian canario beans –</p></div>
      <div class="item"><div class="item-head"><span class="name">AJI DE GALLINA</span><span>11.95</span></div><p class="desc">shredded chicken in a spicy aji amarillo creamy sauce, hard-boiled egg, olives, potatoes and rice –</p></div>
    </div>
    <div class="photo" role="img" aria-label="Photo of a seafood stir-fry with shrimp, calamari and peppers" style="top:478px;bottom:0;background:radial-gradient(ellipse at 50% 60%,#d9874a 0%,#ecd3bb 55%,var(--plate) 100%)"></div>
    <svg class="curve" style="top:464px;height:36px" viewBox="0 0 261 36" preserveAspectRatio="none" aria-hidden="true">
      <path d="M0 0H261V30C180 8 80 4 0 18Z" fill="var(--wood-dark)"/>
      <path d="M0 18C80 4 180 8 261 30V36C180 14 80 10 0 24Z" fill="var(--leaf)"/>
    </svg>
  </div>
</section>

</body>
</html>
```